Tavenorix - world unique technology for better life - please let them know who am i at first sight

We need a new business card for company which is a provider of unique crystal based technology suitable for all living being. For more information and final design you can use our brochure (our colours are black and blue from brochure).
We use Verdana font

Industry/Entity Type

Business

Contact Information for Business Card

regular dimension

Font styles to use
Other font styles liked:
• Verdana

Requirements
Must have
• Logo
• name
• function/position
• phone
• mobile
• e-mail
• adress
Nice to have
• inovative design (technology directed)

```html
<!DOCTYPE html>
<html lang="en">
<head>
<meta charset="utf-8">
<title>Tavenorix Technologies – Business Card</title>
<link rel="stylesheet" href="https://fonts.googleapis.com/css2?family=Open+Sans:wght@400;600;700&display=swap">
<style>
  :root {
    --stage: #e9e4d6;
    --card-black: #0b0b0c;
    --card-white: #f7f7f7;
    --card-white-edge: #dcdcdc;
    --brand-blue: #1ba6e3;
    --silver-light: #e6e6e6;
    --silver-dark: #8d8d8d;
    --text-light: #f2f2f2;
    --text-dark: #3a3a3a;
  }
  * { margin: 0; padding: 0; box-sizing: border-box; }
  html, body {
    width: 1200px; height: 978px; overflow: hidden;
    background: var(--stage);
    font-family: Verdana, "Open Sans", sans-serif;
  }
  .canvas {
    position: relative; width: 1200px; height: 978px;
    display: flex; flex-direction: column; align-items: center; justify-content: center; gap: 40px;
  }
  .card {
    position: relative; width: 760px; height: 434px;
    border-radius: 24px; overflow: hidden;
    box-shadow: 0 6px 18px rgba(0,0,0,0.18);
  }

  /* Front: white card */
  .card--front {
    background: linear-gradient(160deg, var(--card-white) 0%, #ffffff 45%, var(--card-white-edge) 100%);
    display: flex; flex-direction: column; align-items: center; justify-content: center;
  }
  .front-brand { display: flex; align-items: center; gap: 22px; margin-bottom: 70px; }
  .brand-dot { width: 64px; height: 64px; border-radius: 50%; background: var(--brand-blue); }
  .front-brand .brand-name {
    font-size: 64px; font-weight: 400; color: var(--brand-blue); letter-spacing: 2px;
  }
  .front-url {
    font-size: 24px; font-weight: 700; color: var(--text-dark); letter-spacing: 3px;
  }

  /* Back: black card */
  .card--back { background: var(--card-black); }
  .back-waves { position: absolute; inset: 0; }
  .back-brand {
    position: absolute; left: 300px; top: 56px;
    display: flex; align-items: center; gap: 18px;
  }
  .back-brand .brand-dot { width: 46px; height: 46px; }
  .back-brand .brand-name {
    font-size: 40px; font-weight: 400; color: var(--brand-blue); letter-spacing: 3px; line-height: 1.1;
  }
  .back-brand .brand-name span { display: block; font-size: 19px; letter-spacing: 9px; }
  .person {
    position: absolute; right: 440px; top: 176px; text-align: right; color: var(--text-light);
    font-size: 15px; line-height: 1.55;
  }
  .person .person-name { font-size: 22px; font-weight: 700; color: var(--brand-blue); letter-spacing: 0.5px; }
  .person .person-role { margin-bottom: 4px; }
  .divider {
    position: absolute; left: 342px; top: 178px; width: 1px; height: 112px; background: #6b6b6b;
  }
  .contacts {
    position: absolute; left: 362px; top: 180px; list-style: none;
    color: var(--text-light); font-size: 15px;
  }
  .contacts li { display: flex; align-items: center; gap: 10px; height: 34px; }
  .contacts svg { width: 18px; height: 18px; fill: var(--text-light); flex: none; }
  .back-url {
    position: absolute; left: 36px; bottom: 30px;
    color: #ffffff; font-size: 20px; font-weight: 600; letter-spacing: 3px;
  }
</style>
</head>
<body>
<main class="canvas">

  <section class="card card--front" aria-label="Business card front">
    <div class="front-brand">
      <span class="brand-dot"></span>
      <span class="brand-name">Tavenorix</span>
    </div>
    <p class="front-url">www.tavenorix.cu</p>
  </section>

  <section class="card card--back" aria-label="Business card back">
    <svg class="back-waves" viewBox="0 0 760 434" preserveAspectRatio="none" aria-hidden="true">
      <defs>
        <linearGradient id="silverSweep" x1="0" y1="0" x2="1" y2="0">
          <stop offset="0" stop-color="var(--silver-dark)"/>
          <stop offset="0.45" stop-color="var(--silver-light)"/>
          <stop offset="1" stop-color="var(--silver-dark)"/>
        </linearGradient>
      </defs>
      <path d="M0,300 C220,296 420,360 760,382 L760,434 L0,434 Z" fill="url(#silverSweep)"/>
      <path d="M0,322 C230,320 430,384 760,400 L760,434 L0,434 Z" fill="var(--brand-blue)"/>
    </svg>

    <div class="back-brand">
      <span class="brand-dot"></span>
      <p class="brand-name">TAVENORIX<span>TECHNOLOGIES</span></p>
    </div>

    <div class="person">
      <p class="person-name">Mirela Kostanic</p>
      <p class="person-role">Founder and CEO</p>
      <p>Street Name, City Name</p>
      <p>Zipcode-01234</p>
    </div>

    <div class="divider"></div>

    <ul class="contacts">
      <li>
        <svg viewBox="0 0 24 24"><path d="M6.6 10.8a15 15 0 0 0 6.6 6.6l2.2-2.2a1 1 0 0 1 1-.25 11.4 11.4 0 0 0 3.6.57 1 1 0 0 1 1 1V20a1 1 0 0 1-1 1A17 17 0 0 1 3 4a1 1 0 0 1 1-1h3.5a1 1 0 0 1 1 1c0 1.25.2 2.45.57 3.57a1 1 0 0 1-.25 1z"/></svg>
        012-345-6789
      </li>
      <li>
        <svg viewBox="0 0 24 24"><path d="M7 2h10a2 2 0 0 1 2 2v16a2 2 0 0 1-2 2H7a2 2 0 0 1-2-2V4a2 2 0 0 1 2-2zm0 3v13h10V5zm5 14.2a1 1 0 1 0 0 .01z"/></svg>
        012-345-6789
      </li>
      <li>
        <svg viewBox="0 0 24 24"><path d="M3 5h18a1 1 0 0 1 1 1v12a1 1 0 0 1-1 1H3a1 1 0 0 1-1-1V6a1 1 0 0 1 1-1zm1 2.3V17h16V7.3l-8 5.2z"/></svg>
        info@tavenorix.com
      </li>
    </ul>

    <p class="back-url">www.tavenorix.cu</p>
  </section>

</main>
</body>
</html>
```